I need to rebrand my public user portal for a new/modern look and feel

I want to take my current user web portal and redesign the look of it. I have included 2 samples of my current user portal and would like options to create a new functional look. This main page below will modify based on the tabs on the top left. Any questions please ask.

```html
<!DOCTYPE html>
<html lang="en">
<head>
<meta charset="utf-8">
<title>Student Portal Dashboard</title>
<link href="https://fonts.googleapis.com/css2?family=Nunito+Sans:wght@400;500;600;700&display=swap" rel="stylesheet">
<style>
:root{
  --page:#0b1a2e;
  --sidebar:#10264a;
  --nav-active:#1c3866;
  --topsearch:#1b2f4b;
  --card:#ffffff;
  --ink:#1d2430;
  --muted:#8a919c;
  --line:#e7e9ee;
  --thead:#f8f9fb;
  --empty:#f0f4f9;
  --field:#f2f3f5;
  --blue:#2f74c9;
  --red:#e5484d;
}
*{box-sizing:border-box;margin:0;padding:0}
html,body{width:1200px;height:853px;overflow:hidden}
body{background:var(--page);font-family:"Nunito Sans",sans-serif;color:var(--ink);position:relative}
.sidebar{position:absolute;left:0;top:0;width:238px;height:853px;background:var(--sidebar)}
.brand{position:absolute;left:46px;top:36px;display:flex;align-items:center;gap:8px;color:#fff;font-weight:700;font-size:15px}
.brand-mark{width:22px;height:22px;border-radius:50%;background:#fff}
.nav{position:absolute;left:12px;top:138px;width:215px;list-style:none}
.nav li{height:42px;margin-bottom:18px;display:flex;align-items:center;gap:10px;padding-left:36px;color:#fff;font-size:12px;border-radius:5px}
.nav li.active{background:var(--nav-active)}
.nav svg{width:17px;height:17px;fill:none;stroke:#fff;stroke-width:1.6}
.topsearch{position:absolute;left:279px;top:30px;width:248px;height:40px;border-radius:8px;background:var(--topsearch);display:flex;align-items:center;gap:9px;padding-left:14px;color:#fff;font-size:12px}
.topsearch svg{width:16px;height:16px;fill:none;stroke:#fff;stroke-width:1.8}
.user{position:absolute;left:1010px;top:32px;display:flex;align-items:center;color:#fff;font-size:12px}
.user .bell{width:18px;height:18px;fill:none;stroke:#fff;stroke-width:1.6;margin-right:24px}
.avatar{width:36px;height:36px;border-radius:50%;background:linear-gradient(135deg,#c9c3bd,#5b4a44);margin-left:14px}
.caret{margin-left:6px;width:0;height:0;border-left:4px solid transparent;border-right:4px solid transparent;border-top:6px solid #fff}
.card{position:absolute;left:279px;width:888px;background:var(--card);border-radius:4px;overflow:hidden}
.card-title{position:absolute;left:46px;top:40px;font-size:17px;font-weight:500}
.field{position:absolute;left:399px;top:30px;width:247px;height:40px;border-radius:8px;background:var(--field);display:flex;align-items:center;gap:10px;padding-left:16px;color:var(--muted);font-size:12px}
.field svg{width:16px;height:16px;fill:none;stroke:var(--muted);stroke-width:1.8}
.filter{position:absolute;left:670px;top:30px;height:40px;display:flex;align-items:center;gap:10px;font-size:12px;font-weight:600}
.filter svg{width:14px;height:12px;stroke:var(--ink);stroke-width:1.6}
.add{position:absolute;left:740px;top:30px;width:121px;height:40px;border-radius:3px;background:var(--blue);color:#fff;font-size:12px;font-weight:600;display:flex;align-items:center;justify-content:center;gap:10px}
.add svg{width:16px;height:16px;stroke:#fff;stroke-width:1.8}
.table{position:absolute;left:28px;top:90px;width:849px}
.row{position:relative;height:36px;border-bottom:1px solid var(--line);font-size:11px;display:flex;align-items:center}
.row.head{background:var(--thead);font-weight:600;font-size:11.5px}
.row span{position:absolute}
.c-name{left:88px}.c-grade{left:393px}.c-year{left:496px}.c-school{left:606px}
.check{position:absolute;left:25px;width:16px;height:16px;border:1.5px solid #222;border-radius:4px}
.check.on{background:var(--blue);border-color:var(--blue)}
.check.on svg{width:13px;height:13px;stroke:#fff;stroke-width:2;fill:none}
.kebab{position:absolute;left:807px;width:18px;height:18px;border:1px solid var(--line);border-radius:3px;display:flex;align-items:center;justify-content:center}
.kebab.open{background:#dce8f6;border-color:#dce8f6}
.kebab i{display:block;width:2px;height:9px;background:radial-gradient(circle,#333 1px,transparent 1.2px) 0 0/2px 3.5px}
.empty{height:98px;background:var(--empty);display:flex;flex-direction:column;align-items:center;justify-content:center;gap:12px;font-size:11.5px}
.empty svg{width:28px;height:28px;fill:none;stroke:var(--blue);stroke-width:2}
.menu{position:absolute;left:1070px;top:300px;width:103px;height:100px;background:#fff;border-radius:4px;box-shadow:0 4px 14px rgba(0,0,0,.18);padding:14px 0 0 20px;list-style:none}
.menu li{display:flex;align-items:center;gap:8px;font-size:12px;color:var(--blue);height:27px}
.menu li.danger{color:var(--red)}
.menu svg{width:14px;height:14px;fill:none;stroke:currentColor;stroke-width:1.6}
</style>
</head>
<body>
<aside class="sidebar">
  <div class="brand"><span class="brand-mark"></span>Northgate Systems</div>
  <ul class="nav">
    <li class="active"><svg viewBox="0 0 20 20" style="fill:#fff;stroke:none"><path d="M10 2 1 10h3v8h5v-5h2v5h5v-8h3z"/></svg>Dashboard</li>
    <li><svg viewBox="0 0 20 20"><rect x="5" y="3" width="10" height="14" rx="1"/><path d="M5 5H2v10h3M15 5h3v10h-3"/></svg>Application</li>
    <li><svg viewBox="0 0 20 20"><path d="M4 2h8l4 4v12H4z"/><path d="M12 2v4h4"/></svg>Transcipt Request</li>
    <li><svg viewBox="0 0 20 20"><rect x="3" y="9" width="14" height="9"/><path d="M5 6h10M7 3h6"/></svg>New Hire Packet</li>
  </ul>
</aside>

<div class="topsearch"><svg viewBox="0 0 20 20"><circle cx="8.5" cy="8.5" r="6"/><path d="m13 13 5 5"/></svg>Search</div>
<div class="user">
  <svg class="bell" viewBox="0 0 20 20"><path d="M5 14V9a5 5 0 0 1 10 0v5l1.5 2h-13zM8 18h4"/></svg>
  Marla q
  <div class="avatar" role="img" aria-label="User profile photo"></div>
  <div class="caret"></div>
</div>

<section class="card" style="top:107px;height:270px">
  <h2 class="card-title">NGSDEMO19</h2>
  <div class="field"><svg viewBox="0 0 20 20"><circle cx="8.5" cy="8.5" r="6"/><path d="m13 13 5 5"/></svg>Search</div>
  <div class="filter"><svg viewBox="0 0 14 12"><path d="M0 2h14M3 6h8M5.5 10h3"/></svg>Filter</div>
  <div class="add"><svg viewBox="0 0 16 16"><path d="M8 0v16M0 8h16"/></svg>Add Student</div>
  <div class="table">
    <div class="row head"><i class="check"></i><span class="c-name">Name</span><span class="c-grade">Grade</span><span class="c-year">Year</span><span class="c-school">School</span></div>
    <div class="row"><i class="check on"><svg viewBox="0 0 14 14"><path d="m3 7 3 3 5-6"/></svg></i><span class="c-name">Marla Quinnell</span><span class="c-grade">10</span><span class="c-year">2025</span><span class="c-school">Brookfield High School</span><div class="kebab"><i></i></div></div>
    <div class="row"><i class="check"></i><span class="c-name">Dorian Pike</span><span class="c-grade">08</span><span class="c-year">2025</span><span class="c-school">Brookfield High School</span><div class="kebab open"><i></i></div></div>
    <div class="row"><i class="check"></i><span class="c-name">Elliot Varga</span><span class="c-grade">08</span><span class="c-year">2025</span><span class="c-school">Brookfield High School</span></div>
  </div>
</section>

<section class="card" style="top:397px;height:254px">
  <h2 class="card-title">County Vocational School</h2>
  <div class="field"><svg viewBox="0 0 20 20"><circle cx="8.5" cy="8.5" r="6"/><path d="m13 13 5 5"/></svg>Search</div>
  <div class="filter"><svg viewBox="0 0 14 12"><path d="M0 2h14M3 6h8M5.5 10h3"/></svg>Filter</div>
  <div class="add"><svg viewBox="0 0 16 16"><path d="M8 0v16M0 8h16"/></svg>Add Student</div>
  <div class="table">
    <div class="row head"><i class="check"></i><span class="c-name">Name</span><span class="c-grade">Grade</span><span class="c-year">Year</span><span class="c-school">School</span></div>
    <div class="empty"><svg viewBox="0 0 28 28"><circle cx="14" cy="14" r="12.5"/><path d="M14 7.5v8.5M14 19.5v1.5"/></svg>No students found. Please add a new student.</div>
  </div>
</section>

<section class="card" style="top:672px;height:200px">
  <h2 class="card-title">Progress Demo School</h2>
  <div class="field"><svg viewBox="0 0 20 20"><circle cx="8.5" cy="8.5" r="6"/><path d="m13 13 5 5"/></svg>Search</div>
  <div class="filter"><svg viewBox="0 0 14 12"><path d="M0 2h14M3 6h8M5.5 10h3"/></svg>Filter</div>
  <div class="add"><svg viewBox="0 0 16 16"><path d="M8 0v16M0 8h16"/></svg>Add Student</div>
  <div class="table">
    <div class="row head"><i class="check"></i><span class="c-name">Name</span><span class="c-grade">Grade</span><span class="c-year">Year</span><span class="c-school">School</span></div>
    <div class="empty" style="justify-content:flex-start;padding-top:15px"><svg viewBox="0 0 28 28"><circle cx="14" cy="14" r="12.5"/><path d="M14 7.5v8.5M14 19.5v1.5"/></svg></div>
  </div>
</section>

<ul class="menu">
  <li><svg viewBox="0 0 16 16"><path d="M3 13 2.5 10 10 2.5l3 3L5.5 13zM2 15h12"/></svg>Edit</li>
  <li><svg viewBox="0 0 16 16"><rect x="2" y="2.5" width="12" height="11" rx="1.5"/><path d="M2 6h12M6 9h4"/></svg>Archive</li>
  <li class="danger"><svg viewBox="0 0 16 16"><path d="M2 4h12M6 4V2h4v2M4 4l1 10h6l1-10"/></svg>Delete</li>
</ul>
</body>
</html>
```